I am looking for a modern, clean and neat design for a reflexology and well being business. The business name is Lumen Orto (this is an old Latin word for wellbeing). The colours I would like are purple, white and grey. I am open to suggestions for pictures such as healing or working hands, a pair of feet, images that represent my business that you may think of....... or maybe you think no images at all would be best? My tag line is: "Find your balance" or "Find you balance......... Find your balance" I can decide which I want so I would like to see what both would look like. I would like space on the back to write the client's appointment date and time (more than once)

```html
<!DOCTYPE html>
<html lang="en">
<head>
<meta charset="utf-8">
<title>Lumen Orto – Business Card</title>
<link rel="stylesheet" href="https://fonts.googleapis.com/css2?family=Open+Sans:wght@400;600&display=swap">
<style>
  :root {
    --stage: #3c3c3c;
    --white: #ffffff;
    --purple: #8e2490;
    --purple-deep: #7d2280;
    --purple-end: #6e2170;
    --silver-light: #e6e6e6;
    --silver: #a9a9a9;
    --ink: #1a1a1a;
    --ink-soft: #555555;
    --text-light: #f4eef4;
  }
  * { margin: 0; padding: 0; box-sizing: border-box; }
  html, body {
    width: 1200px;
    height: 675px;
    overflow: hidden;
    background: var(--stage);
  }
  .stage {
    position: relative;
    width: 1200px;
    height: 675px;
  }
  .card {
    position: absolute;
    width: 464px;
    height: 264px;
    background: var(--white);
    overflow: hidden;
  }
  .card--front { left: 175px; top: 114px; z-index: 2; }
  .card--back  { left: 540px; top: 314px; z-index: 1; }

  .silver-rule {
    position: absolute;
    left: 0;
    width: 100%;
    height: 4px;
    background: linear-gradient(90deg, var(--silver) 0%, var(--silver-light) 50%, var(--silver) 100%);
  }
  .stripe-band {
    position: absolute;
    left: 0;
    width: 100%;
    background: repeating-linear-gradient(90deg,
      var(--purple) 0px, var(--purple) 24px,
      var(--purple-deep) 24px, var(--purple-deep) 38px);
  }

  .brand-name {
    font-family: "Open Sans", sans-serif;
    font-weight: 400;
    line-height: 1;
  }
  .brand-tagline {
    font-family: "Open Sans", sans-serif;
    font-weight: 400;
    text-transform: uppercase;
    line-height: 1;
    white-space: nowrap;
  }

  /* Front */
  .card--front .silver-rule--top { top: 36px; }
  .card--front .stripe-band { top: 40px; height: 186px; }
  .card--front .silver-rule--bottom { top: 226px; }
  .front-brand {
    position: absolute;
    left: 0; right: 0;
    top: 40px;
    height: 186px;
    display: flex;
    flex-direction: column;
    align-items: center;
    justify-content: center;
  }
  .front-brand .brand-name {
    font-size: 37px;
    color: var(--text-light);
  }
  .front-brand .brand-tagline {
    margin-top: 11px;
    font-size: 16px;
    letter-spacing: 2.4px;
    color: var(--white);
  }

  /* Back */
  .back-brand {
    position: absolute;
    right: 50px;
    top: 44px;
    text-align: left;
  }
  .back-brand .brand-name {
    font-size: 27px;
    color: var(--ink);
  }
  .back-brand .brand-tagline {
    margin-top: 12px;
    font-size: 12px;
    font-weight: 600;
    letter-spacing: 1.8px;
    color: var(--ink-soft);
  }
  .appointment {
    position: absolute;
    left: 36px;
    top: 138px;
    list-style: none;
    font-family: "Open Sans", sans-serif;
    font-size: 10.5px;
    font-weight: 600;
    letter-spacing: 0.6px;
    color: var(--ink-soft);
  }
  .appointment li { height: 25px; }
  .card--back .silver-rule--top { top: 187px; }
  .card--back .stripe-band { top: 191px; height: 73px; }
  .card--back .stripe-band::after {
    content: "";
    position: absolute;
    right: 0; top: 0;
    width: 42px; height: 100%;
    background: var(--purple-end);
  }
</style>
</head>
<body>
<main class="stage">
  <section class="card card--front" aria-label="Card front">
    <div class="silver-rule silver-rule--top"></div>
    <div class="stripe-band"></div>
    <div class="silver-rule silver-rule--bottom"></div>
    <div class="front-brand">
      <h1 class="brand-name">Lumen Orto</h1>
      <p class="brand-tagline">Find your balance</p>
    </div>
  </section>

  <section class="card card--back" aria-label="Card back">
    <div class="back-brand">
      <h2 class="brand-name">Lumen Orto</h2>
      <p class="brand-tagline">Find your balance</p>
    </div>
    <ul class="appointment">
      <li>Appointment Date:</li>
      <li>Time:</li>
    </ul>
    <div class="silver-rule silver-rule--top"></div>
    <div class="stripe-band"></div>
  </section>
</main>
</body>
</html>
```